Reworking our Ayurvedic Tea Boxes with Mordern and New look.

We are a Tea Wholesale company for retailers and health food stores. We have currently a Ayurvedic wellness tea line needs an updated packaging. We would like to see new modern, clean and beautiful new fresh look. Our current packaging can be seen at http://leafmerchantco.example/c/7720815/1/herbal-blends.html

We are going to launch various categories in the loose leaf tea line. This is just the first step. At present 9 different exsit in the wellnes line.
Updates

Target Market(s)

Health Food Stores, Specialty Food Stores, Grocery Stores.

Industry/Entity Type

It Company

Requirements
Must have
• - Name of the of the tea type should be clearly visible.
• - A modern fresh look. Not to heavy with design work.
Nice to have
• Box size is 8 cm (L) X 4.5 cm (W) X 15cm (H)

```html
<!DOCTYPE html>
<html lang="en">
<head>
<meta charset="utf-8">
<title>Tea Reverie – Morning Blend Packaging</title>
<link href="https://fonts.googleapis.com/css2?family=Source+Sans+3:wght@400;600&display=swap" rel="stylesheet">
<style>
  :root {
    --stage: #ececec;
    --paper: #ffffff;
    --lime: #b9c52f;
    --lime-light: #d3da62;
    --lime-deep: #a8b61f;
    --leaf-yellow: #e6e82e;
    --leaf-pale: #f6f7cf;
    --ink: #1b2418;
    --ink-soft: #ffffff;
    --ink-dark: #2a3412;
    --rule: #c2cc3a;
  }
  * { box-sizing: border-box; margin: 0; padding: 0; }
  html, body {
    width: 1200px; height: 1000px; overflow: hidden;
    background: var(--stage);
    font-family: "Source Sans 3", "Helvetica Neue", Arial, sans-serif;
  }
  .canvas { position: relative; width: 1200px; height: 1000px; }

  .dieline {
    position: absolute; left: 250px; top: 80px;
    display: flex; height: 840px;
    box-shadow: 0 10px 30px rgba(0,0,0,0.12);
  }
  .panel { position: relative; height: 840px; background: var(--paper); overflow: hidden; }
  .panel--front { width: 448px; }
  .panel--side { width: 252px; border-left: 1px solid #dcdcdc; }

  /* top white zone */
  .brand-zone { position: absolute; left: 0; right: 0; top: 0; height: 250px; }
  .brand-name {
    position: absolute; left: 0; right: 0; text-align: center;
    font-weight: 600; color: var(--ink); letter-spacing: 1px;
  }
  .panel--front .brand-name { top: 128px; font-size: 58px; }
  .brand-dot {
    position: absolute; left: 50%; transform: translateX(-50%);
    border-radius: 50%; background: var(--lime);
  }
  .panel--front .brand-dot { top: 44px; width: 64px; height: 64px; }
  .panel--side .brand-dot { top: 26px; width: 38px; height: 38px; }
  .panel--side .brand-name { top: 74px; font-size: 34px; }

  .side-info { position: absolute; left: 0; right: 0; top: 130px; text-align: center; color: var(--ink); }
  .side-info .type { font-size: 14px; font-weight: 600; letter-spacing: 0.2px; }
  .side-info .blend { font-size: 22px; font-weight: 400; margin-top: 6px; color: #4a5a1a; }
  .side-info .mantra { font-size: 14px; font-weight: 600; margin-top: 4px; }

  /* bands */
  .band-rule { position: absolute; left: 0; right: 0; top: 250px; height: 10px; background: var(--rule); }
  .band-ornament {
    position: absolute; left: 0; right: 0; top: 266px; height: 44px;
    background: linear-gradient(180deg, var(--lime-light), var(--lime));
  }
  .field {
    position: absolute; left: 0; right: 0; top: 310px; bottom: 0;
    background: linear-gradient(180deg, var(--lime) 0%, var(--lime-deep) 100%);
  }

  /* front texts */
  .front-copy { position: absolute; left: 64px; top: 372px; color: var(--ink-soft); z-index: 2; }
  .front-copy .type { font-size: 19px; line-height: 1.35; }
  .front-copy .bullet { width: 7px; height: 7px; border-radius: 50%; background: var(--ink-soft); margin: 12px 0 12px 58px; }
  .front-copy .blend { font-size: 44px; line-height: 1.05; font-weight: 400; }
  .front-copy .mantra { font-size: 18px; color: var(--ink-dark); }
  .net-weight { position: absolute; left: 64px; bottom: 40px; font-size: 17px; line-height: 1.3; color: var(--ink-dark); z-index: 2; }

  /* leaf artwork areas */
  .leaf-art {
    position: absolute; border-radius: 14px;
    background: linear-gradient(160deg, var(--leaf-yellow) 0%, var(--leaf-pale) 45%, var(--leaf-yellow) 75%, #d8dc2c 100%);
  }
  .panel--front .leaf-art { left: 250px; top: 440px; width: 172px; height: 380px; }
  .panel--side .leaf-art { left: 22px; top: 392px; width: 208px; height: 430px; }
</style>
</head>
<body>
<main class="canvas">
  <section class="dieline">
    <article class="panel panel--front">
      <header class="brand-zone">
        <span class="brand-dot"></span>
        <h1 class="brand-name">Tea Reverie</h1>
      </header>
      <div class="band-rule"></div>
      <div class="band-ornament" role="img" aria-label="White paisley ornament border"></div>
      <div class="field"></div>
      <div class="leaf-art" role="img" aria-label="Pattern of stylised yellow and white tea leaves"></div>
      <div class="front-copy">
        <p class="type">LOOSE LEAF<br>AYURVEDIC TEA</p>
        <div class="bullet"></div>
        <h2 class="blend">Morning<br>Blend</h2>
        <div class="bullet"></div>
        <p class="mantra">Surya Namaskar</p>
      </div>
      <p class="net-weight">Net Wt.<br>100 g/ 3.5 oz</p>
    </article>

    <article class="panel panel--side">
      <header class="brand-zone">
        <span class="brand-dot"></span>
        <h2 class="brand-name">Tea Reverie</h2>
        <div class="side-info">
          <p class="type">LOOSE LEAF AYURVEDIC TEA</p>
          <p class="blend">Morning Blend</p>
          <p class="mantra">Surya Namaskar</p>
        </div>
      </header>
      <div class="band-rule"></div>
      <div class="band-ornament" role="img" aria-label="White paisley ornament border"></div>
      <div class="field"></div>
      <div class="leaf-art" role="img" aria-label="Pattern of stylised yellow and white tea leaves"></div>
    </article>
  </section>
</main>
</body>
</html>
```